New Business Cards for Organic Meat Farm

We need a business card designed for Thornbury Farm, a meat farm in western MA. Our logo uses a hand-drawn woodcut (attached). Our color palette has been simply black and white (shown in notepad and picture of our food truck). While we are based out of western MA, we have ambitions to grow nationally, so our hope is for a classy and memorable card which will be printed on a premium quality stock from a printer like printkestrel.com.
Target Market(s)
consumers of quality meats, restauranteurs, partnering farms
Industry/Entity Type
Farming and prepared meat products
Contact Information for Business Card
Wendell Pruitt, President/Owner, wendell@thornburyfarm.com, mobile: 413-555-0172, phone: 413-555-0148, thornburyfarm.com, facebook: @thornburyfarm, instagram: @thornburyfarmma
Colors
Designer to choose colors to be used in the design.
Look and feel

```html
<!DOCTYPE html>
<html lang="en">
<head>
<meta charset="utf-8">
<title>Thornbury Farm — Business Card</title>
<link rel="stylesheet" href="https://fonts.googleapis.com/css2?family=Playfair+Display:ital,wght@0,500;0,600;1,500&family=Tinos&family=Poppins:wght@300&display=swap">
<style>
  :root {
    --backdrop: #b8b4b1;
    --paper: #ece7e4;
    --ink: #000000;
    --ink-soft: #1a1a1a;
    --light: #f2efec;
    --rule: #8a8a8a;
  }
  * { margin: 0; padding: 0; box-sizing: border-box; }
  html, body {
    width: 1200px; height: 1112px; overflow: hidden;
    background: var(--backdrop);
  }
  .canvas { position: relative; width: 1200px; height: 1112px; }

  .card { position: absolute; width: 753px; height: 442px; }

  /* Front */
  .card--front {
    left: 73px; top: 75px;
    background: var(--paper);
    display: flex; align-items: center; justify-content: center;
  }
  .brand-name {
    font-family: "Playfair Display", serif;
    font-weight: 600;
    font-size: 44px;
    color: var(--ink-soft);
    letter-spacing: 0.5px;
  }

  /* Back */
  .card--back {
    left: 372px; top: 592px;
    background: var(--ink);
    display: flex;
  }
  .back-main { position: relative; width: 648px; height: 100%; color: var(--light); }
  .person { position: absolute; left: 44px; top: 44px; }
  .person-name {
    font-family: "Playfair Display", serif;
    font-weight: 500; font-size: 33px; line-height: 1.1; letter-spacing: 0.5px;
  }
  .person-title {
    font-family: "Playfair Display", serif;
    font-style: italic; font-weight: 500; font-size: 26px; line-height: 1.3; margin-top: 2px;
  }
  .divider {
    position: absolute; left: 44px; top: 126px;
    width: 557px; height: 2px; background: var(--rule);
  }
  .contacts {
    position: absolute; left: 44px; top: 325px;
    display: grid; grid-template-columns: 237px auto; row-gap: 8px;
    font-family: "Tinos", serif; font-size: 23px;
  }
  .contact { display: flex; align-items: center; height: 31px; }
  .contact svg { width: 20px; height: 20px; margin-right: 21px; fill: var(--light); flex: none; }

  .back-side { position: relative; width: 105px; height: 100%; background: var(--paper); }
  .social-strip { display: block; width: 105px; height: 442px; }
  .social-handle {
    font-family: "Poppins", sans-serif; font-weight: 300; font-size: 17px;
    fill: var(--ink);
  }
  .social-dot { fill: var(--ink); }
</style>
</head>
<body>
<main class="canvas">
  <section class="card card--front" aria-label="Card front">
    <span class="brand-name">Thornbury Farm</span>
  </section>

  <section class="card card--back" aria-label="Card back">
    <div class="back-main">
      <div class="person">
        <p class="person-name">Wendell Pruitt</p>
        <p class="person-title">President/Owner</p>
      </div>
      <div class="divider"></div>
      <div class="contacts">
        <div class="contact">
          <svg viewBox="0 0 24 24" aria-hidden="true"><path d="M6.6 10.8a15.1 15.1 0 0 0 6.6 6.6l2.2-2.2a1 1 0 0 1 1-.25 11.4 11.4 0 0 0 3.6.6 1 1 0 0 1 1 1V20a1 1 0 0 1-1 1A17 17 0 0 1 3 4a1 1 0 0 1 1-1h3.5a1 1 0 0 1 1 1c0 1.25.2 2.45.6 3.6a1 1 0 0 1-.25 1z"/></svg>
          <span>413-555-0148</span>
        </div>
        <div class="contact">
          <svg viewBox="0 0 24 24" aria-hidden="true"><path d="M12 2 2 8.5V20a1 1 0 0 0 1 1h18a1 1 0 0 0 1-1V8.5zm0 2.4 7.6 4.9L12 13.6 4.4 9.3z"/></svg>
          <span>wendell@thornburyfarm.com</span>
        </div>
        <div class="contact">
          <svg viewBox="0 0 24 24" aria-hidden="true"><path d="M16 1H8a2.5 2.5 0 0 0-2.5 2.5v17A2.5 2.5 0 0 0 8 23h8a2.5 2.5 0 0 0 2.5-2.5v-17A2.5 2.5 0 0 0 16 1zm0 18H8V4h8zm-4 3a1 1 0 1 1 0-2 1 1 0 0 1 0 2z"/></svg>
          <span>413-555-0172</span>
        </div>
        <div class="contact">
          <svg viewBox="0 0 24 24" aria-hidden="true"><path d="M12 2a10 10 0 1 0 0 20 10 10 0 0 0 0-20zm6.9 6h-2.9a15.7 15.7 0 0 0-1.4-3.6A8 8 0 0 1 18.9 8zM12 4c.8 1.2 1.5 2.5 1.9 4h-3.8c.4-1.5 1.1-2.8 1.9-4zM4.3 14a8 8 0 0 1 0-4h3.4a16 16 0 0 0 0 4zm.8 2h2.9c.3 1.3.8 2.5 1.4 3.6A8 8 0 0 1 5.1 16zM8 8H5.1a8 8 0 0 1 4.3-3.6C8.8 5.5 8.3 6.7 8 8zm4 12c-.8-1.2-1.5-2.5-1.9-4h3.8c-.4 1.5-1.1 2.8-1.9 4zm2.3-6H9.7a14.7 14.7 0 0 1 0-4h4.6a14.7 14.7 0 0 1 0 4zm.3 5.6c.6-1.1 1.1-2.3 1.4-3.6h2.9a8 8 0 0 1-4.3 3.6zm1.7-5.6a16 16 0 0 0 0-4h3.4a8 8 0 0 1 0 4z"/></svg>
          <span>thornburyfarm.com</span>
        </div>
      </div>
    </div>
    <div class="back-side">
      <svg class="social-strip" viewBox="0 0 105 442" aria-label="Social handles">
        <circle class="social-dot" cx="52" cy="405" r="6"/>
        <text class="social-handle" transform="translate(58 390) rotate(-90)">@thornburyfarm</text>
        <circle class="social-dot" cx="52" cy="211" r="6"/>
        <text class="social-handle" transform="translate(58 196) rotate(-90)">@thornburyfarmma</text>
      </svg>
    </div>
  </section>
</main>
</body>
</html>
```